CV design and layout with option for text and contact details has be sleek

I have logo just need this to look good on a CV

Target Market(s)

Directors , Production , TV, Film

Industry/Entity Type

tv film cinema advertising

Colors
0054AA
0677BA
7BADD7
CADEEF
E8F1F8

Requirements
Must have
• my logo and contact information
Should not have
• any other images or logos except mine

```html
<!DOCTYPE html>
<html lang="en">
<head>
<meta charset="utf-8">
<title>Reid Calloway – Cinematographer CV</title>
<link rel="stylesheet" href="https://fonts.googleapis.com/css2?family=Montserrat:wght@400;500;600;700&display=swap">
<style>
  :root {
    --backdrop: #dcd9da;
    --paper: #ffffff;
    --ink: #0a0a0a;
    --brand-block: #000000;
    --sidebar: #cdeefc;
    --rule: #bfe6f5;
    --on-dark: #ffffff;
  }
  * { margin: 0; padding: 0; box-sizing: border-box; }
  html, body { width: 1000px; height: 1200px; overflow: hidden; }
  body {
    background: var(--backdrop);
    font-family: "Montserrat", sans-serif;
    color: var(--ink);
    position: relative;
  }
  .cv {
    position: absolute; left: 115px; top: 56px;
    width: 770px; height: 1087px;
    background: var(--paper);
  }
  .brand {
    position: absolute; left: 0; top: 0; width: 250px; height: 249px;
    background: var(--brand-block);
    color: var(--on-dark);
  }
  .brand-name {
    position: absolute; left: 0; width: 250px; top: 114px;
    text-align: center;
    font-size: 16px; font-weight: 700; line-height: 20px;
  }
  .sidebar {
    position: absolute; left: 0; top: 249px; width: 250px; height: 838px;
    background: var(--sidebar);
  }
  .side-section { position: absolute; left: 33px; width: 190px; }
  .side-heading { font-size: 13px; font-weight: 700; letter-spacing: 0.4px; line-height: 16px; }
  .side-text { margin-top: 22px; font-size: 11px; font-weight: 500; line-height: 15.6px; }

  .contact {
    position: absolute; left: 474px; top: 61px;
    font-size: 10.5px; font-weight: 400; line-height: 25px;
    display: grid; grid-template-columns: 107px auto;
  }

  .section { position: absolute; left: 277px; width: 458px; }
  .section-heading {
    font-size: 12.5px; font-weight: 700; line-height: 16px;
    padding-bottom: 6px; border-bottom: 1px solid var(--rule);
  }
  .entries { position: relative; }
  .entry-divider { position: absolute; left: 128px; width: 1px; background: var(--rule); }
  .entry { position: absolute; left: 0; width: 458px; font-size: 10.8px; line-height: 15.6px; }
  .entry-meta { position: absolute; left: 0; width: 125px; font-weight: 500; }
  .entry-meta .company, .entry-body .designation { font-weight: 700; }
  .entry-body { position: absolute; left: 147px; width: 320px; font-weight: 500; }
  .entry-body ul { list-style: none; }
  .entry-body li::before { content: "• "; }
</style>
</head>
<body>
<main class="cv">
  <header class="brand">
    <div class="brand-name">Reid Calloway</div>
  </header>

  <aside class="sidebar">
    <section class="side-section" style="top:45px">
      <h2 class="side-heading">ABOUT ME</h2>
      <p class="side-text">Highly skilled Cinematographer with over 10 years of experience in the film industry. Proven ability to work with large teams and manage all aspects of camera operation and maintenance. Strong background in visual storytelling and post-production editing.</p>
    </section>
    <section class="side-section" style="top:551px">
      <h2 class="side-heading">REFERENCE</h2>
      <p class="side-text">Lorem ipsum dolor sit amet, consectetur adipiscing elit, sed do eiusmod tempor incididunt ut labore et dolore magna aliqua. Ut enim ad minim veniam, quis nostrud exercitation ullamco laboris nisi ut aliquip ex ea commodo consequat. Duis aute irure dolor in reprehenderit in</p>
    </section>
  </aside>

  <dl class="contact">
    <dt>Mobile (Australia):</dt><dd>+61 400 555 018</dd>
    <dt>Mobile (USA):</dt><dd>+61 400 555 018</dd>
    <dt>Agent Crewline:</dt><dd>+61 2 5550 1940</dd>
    <dt>Email:</dt><dd>reidcallowaydop@crew.net</dd>
    <dt>Website:</dt><dd>www.reidcalloway.com.au</dd>
  </dl>

  <section class="section" style="top:247px">
    <h2 class="section-heading">WORK EXPERIENCE</h2>
    <div class="entries">
      <span class="entry-divider" style="top:16px;height:304px"></span>
      <article class="entry" style="top:15px">
        <div class="entry-meta"><div class="company">COMPANY NAME</div><div>ADDRESS</div><div>DATES</div></div>
        <div class="entry-body"><div class="designation">DESIGNATION</div>
          <ul>
            <li>Lorem ipsum dolor sit amet, consectetur adipiscing</li>
            <li>Sed do eiusmod tempor incididunt ut labore et dolore</li>
            <li>Magna aliqua. Ut enim ad minim veniam, quis nostrud</li>
            <li>Exercitation ullamco laboris nisi ut aliquip ex ea</li>
            <li>Commodo consequat. Duis aute irure dolor in</li>
            <li>Reprehenderit in voluptate velit esse cillum dolore eu</li>
            <li>Fugiat nulla pariatur. Excepteur sint occaecat</li>
          </ul>
        </div>
      </article>
      <article class="entry" style="top:179px">
        <div class="entry-meta"><div class="company">COMPANY NAME</div><div>ADDRESS</div><div>DATES</div></div>
        <div class="entry-body"><div class="designation">DESIGNATION</div>
          <ul>
            <li>Lorem ipsum dolor sit amet, consectetur adipiscing</li>
            <li>Sed do eiusmod tempor incididunt ut labore et dolore</li>
            <li>Magna aliqua. Ut enim ad minim veniam, quis nostrud</li>
            <li>Exercitation ullamco laboris nisi ut aliquip ex ea</li>
            <li>Commodo consequat. Duis aute irure dolor in</li>
            <li>Reprehenderit in voluptate velit esse cillum dolore eu</li>
            <li>Fugiat nulla pariatur. Excepteur sint occaecat</li>
          </ul>
        </div>
      </article>
    </div>
  </section>

  <section class="section" style="top:649px">
    <h2 class="section-heading">PROJECTS</h2>
    <div class="entries">
      <span class="entry-divider" style="top:16px;height:304px"></span>
      <article class="entry" style="top:15px">
        <div class="entry-meta"><div class="company">COMPANY NAME</div><div>ADDRESS</div><div>DATES</div></div>
        <div class="entry-body"><div class="designation">DESIGNATION</div>
          <ul>
            <li>Lorem ipsum dolor sit amet, consectetur adipiscing</li>
            <li>Sed do eiusmod tempor incididunt ut labore et dolore</li>
            <li>Magna aliqua. Ut enim ad minim veniam, quis nostrud</li>
            <li>Exercitation ullamco laboris nisi ut aliquip ex ea</li>
            <li>Commodo consequat. Duis aute irure dolor in</li>
            <li>Reprehenderit in voluptate velit esse cillum dolore eu</li>
            <li>Fugiat nulla pariatur. Excepteur sint occaecat</li>
          </ul>
        </div>
      </article>
      <article class="entry" style="top:179px">
        <div class="entry-meta"><div class="company">COMPANY NAME</div><div>ADDRESS</div><div>DATES</div></div>
        <div class="entry-body"><div class="designation">DESIGNATION</div>
          <ul>
            <li>Lorem ipsum dolor sit amet, consectetur adipiscing</li>
            <li>Sed do eiusmod tempor incididunt ut labore et dolore</li>
            <li>Magna aliqua. Ut enim ad minim veniam, quis nostrud</li>
            <li>Exercitation ullamco laboris nisi ut aliquip ex ea</li>
            <li>Commodo consequat. Duis aute irure dolor in</li>
            <li>Reprehenderit in voluptate velit esse cillum dolore eu</li>
            <li>Fugiat nulla pariatur. Excepteur sint occaecat</li>
          </ul>
        </div>
      </article>
    </div>
  </section>
</main>
</body>
</html>
```